Sales Flyer

I am looking for a one page 8x11 flyer that I can print and mail to potential customers. I want to get the message across to potential customers that if they purchase a mobile patrol service with my company then I will provide them with a free camera system with installation or intrusion alarm system with install.

I don't photos to add to the flyer but I would like to to have a couple of security related photos. Can the designers obtain applicable photos?

```html
<!DOCTYPE html>
<html lang="en">
<head>
<meta charset="utf-8">
<title>Ironwell Security Group – Patrol Offer Flyer</title>
<link href="https://fonts.googleapis.com/css2?family=Montserrat:wght@500;700;800;900&family=Open+Sans:wght@400;600;700&display=swap" rel="stylesheet">
<style>
  :root{
    --navy:#0b1f45;
    --navy-deep:#071633;
    --blue:#1e6fd9;
    --blue-bright:#2f8cf0;
    --slate:#3c4658;
    --gray-light:#eef1f5;
    --ink:#1c2434;
    --muted:#5a6475;
    --white:#ffffff;
  }
  *{margin:0;padding:0;box-sizing:border-box}
  html,body{width:837px;height:1200px;overflow:hidden;background:#d9dbde}
  .flyer{position:relative;width:837px;height:1200px;background:var(--white);overflow:hidden;font-family:"Open Sans",Arial,sans-serif;color:var(--ink)}
  .backdrop{position:absolute;inset:0}
  .brand{position:absolute;left:54px;top:52px;display:flex;align-items:center;gap:12px}
  .brand-mark{width:30px;height:30px;background:var(--blue)}
  .brand-name{font-family:"Montserrat",Arial,sans-serif;font-weight:800;font-size:21px;color:var(--navy);line-height:1.05;text-transform:uppercase}
  .headline{position:absolute;left:468px;top:70px;width:330px;color:var(--white);text-align:right}
  .headline .kicker{font-size:13px;font-weight:600;color:#b9cdf0;margin-bottom:8px}
  .headline h1{font-family:"Montserrat",Arial,sans-serif;font-weight:900;font-size:44px;line-height:1.02;text-transform:uppercase}
  .headline h1 .accent{color:var(--blue-bright)}
  .photo-monitoring{position:absolute;left:0;top:250px;width:440px;height:285px;background:linear-gradient(135deg,#0d2a5c 0%,#1d5bb5 55%,#0a1a3a 100%);clip-path:polygon(0 0,88% 0,100% 18%,100% 100%,0 100%)}
  .offer{position:absolute;left:44px;top:556px;width:360px}
  .offer p{font-size:13.5px;line-height:1.5;color:var(--muted)}
  .offer h2{font-family:"Montserrat",Arial,sans-serif;font-weight:800;font-size:25px;line-height:1.1;margin-top:12px;color:var(--navy);text-transform:uppercase}
  .offer h2 .accent{display:block;color:var(--blue)}
  .system{position:absolute;left:44px;width:360px;padding:18px 22px}
  .system .tag{font-size:12px;font-weight:600}
  .system h3{font-family:"Montserrat",Arial,sans-serif;font-weight:800;font-size:24px;line-height:1.05;text-transform:uppercase;margin:4px 0 6px}
  .system .note{font-size:12px;line-height:1.4}
  .system-camera{top:704px;background:var(--slate);color:var(--white)}
  .system-camera .tag,.system-camera .note{color:#cfd6e2}
  .system-or{position:absolute;left:44px;top:858px;width:360px;text-align:center;font-family:"Montserrat",Arial,sans-serif;font-weight:800;font-size:16px;color:var(--blue)}
  .system-alarm{top:888px;background:var(--gray-light);color:var(--navy)}
  .system-alarm .note{color:var(--muted)}
  .reasons{position:absolute;left:466px;top:330px;width:330px}
  .reasons .lead{font-family:"Montserrat",Arial,sans-serif;font-weight:700;font-size:18px;color:var(--navy)}
  .reasons h2{font-family:"Montserrat",Arial,sans-serif;font-weight:800;font-size:22px;color:var(--blue);margin-bottom:22px}
  .reasons ul{list-style:none}
  .reasons li{display:flex;gap:14px;margin-bottom:22px;font-size:13px;line-height:1.5;color:var(--muted)}
  .reasons li svg{flex:0 0 26px;margin-top:2px}
  .photo-devices{position:absolute;left:466px;top:800px;width:330px;height:250px;background:linear-gradient(160deg,#f3f5f8 0%,#c9d2de 60%,#8e9bb0 100%)}
  .footer{position:absolute;left:0;bottom:0;width:837px;height:104px;background:var(--navy);display:flex;align-items:center;justify-content:space-between;padding:0 44px;color:var(--white)}
  .contact{display:flex;align-items:center;gap:12px}
  .contact .label{font-size:12px;color:#b9cdf0}
  .contact .value{font-family:"Montserrat",Arial,sans-serif;font-weight:800;font-size:20px}
  .web{font-size:15px;font-weight:600}
</style>
</head>
<body>
<main class="flyer">
  <svg class="backdrop" width="837" height="1200" viewBox="0 0 837 1200" aria-hidden="true">
    <polygon points="440,30 837,30 837,300 480,300 440,260" fill="#0b1f45"/>
    <polygon points="410,30 440,30 440,260 480,300 450,300 410,260" fill="#1e6fd9"/>
    <polygon points="0,1070 837,1050 837,1096 0,1096" fill="#1e6fd9"/>
  </svg>

  <div class="brand">
    <span class="brand-mark"></span>
    <span class="brand-name">Ironwell<br>Security Group</span>
  </div>

  <header class="headline">
    <p class="kicker">Does your business require our</p>
    <h1>Security Guards <span class="accent">or Mobile</span> Patrols?</h1>
  </header>

  <div class="photo-monitoring" role="img" aria-label="Photo of a security officer watching surveillance monitors in a control room"></div>

  <section class="offer">
    <p>Partner with Ironwell Security Group for your guard or mobile patrol services and receive one of the following security systems with</p>
    <h2>Installation <span class="accent">Free of Charge</span></h2>
  </section>

  <div class="system system-camera">
    <p class="tag">Ultra-fast &amp; high resolution</p>
    <h3>Security<br>Camera System</h3>
    <p class="note">Crisp HD video viewable from your phone, day or night.</p>
  </div>
  <div class="system-or">— OR —</div>
  <div class="system system-alarm">
    <h3>Sentrex Intrusion<br>Alarm System</h3>
    <p class="note">Door, window and motion sensors with 24/7 monitored response.</p>
  </div>

  <section class="reasons">
    <p class="lead">Why partner with</p>
    <h2>Ironwell Security Group</h2>
    <ul>
      <li><svg width="26" height="26" viewBox="0 0 26 26"><circle cx="13" cy="13" r="13" fill="#1e6fd9"/><path d="M7.5 13.5l3.5 3.5 7.5-8" stroke="#fff" stroke-width="2.4" fill="none" stroke-linecap="round" stroke-linejoin="round"/></svg><span>Licensed and insured officers trained to protect your property, staff and customers around the clock.</span></li>
      <li><svg width="26" height="26" viewBox="0 0 26 26"><circle cx="13" cy="13" r="13" fill="#1e6fd9"/><path d="M7.5 13.5l3.5 3.5 7.5-8" stroke="#fff" stroke-width="2.4" fill="none" stroke-linecap="round" stroke-linejoin="round"/></svg><span>Mobile patrol routes planned around your site with random checks that keep intruders guessing.</span></li>
      <li><svg width="26" height="26" viewBox="0 0 26 26"><circle cx="13" cy="13" r="13" fill="#1e6fd9"/><path d="M7.5 13.5l3.5 3.5 7.5-8" stroke="#fff" stroke-width="2.4" fill="none" stroke-linecap="round" stroke-linejoin="round"/></svg><span>Detailed reports after every shift so you always know what happened on your premises.</span></li>
      <li><svg width="26" height="26" viewBox="0 0 26 26"><circle cx="13" cy="13" r="13" fill="#1e6fd9"/><path d="M7.5 13.5l3.5 3.5 7.5-8" stroke="#fff" stroke-width="2.4" fill="none" stroke-linecap="round" stroke-linejoin="round"/></svg><span>One trusted local team for guards, patrols, cameras and alarm monitoring.</span></li>
    </ul>
  </section>

  <div class="photo-devices" role="img" aria-label="Photo of a hand holding a smartphone beside a white security camera"></div>

  <footer class="footer">
    <div class="contact">
      <svg width="30" height="30" viewBox="0 0 24 24" aria-hidden="true"><path d="M6.6 10.8a15.1 15.1 0 006.6 6.6l2.2-2.2a1 1 0 011-.25 11.4 11.4 0 003.6.57 1 1 0 011 1V20a1 1 0 01-1 1A17 17 0 013 4a1 1 0 011-1h3.5a1 1 0 011 1c0 1.25.2 2.45.57 3.6a1 1 0 01-.25 1z" fill="#2f8cf0"/></svg>
      <div>
        <p class="label">Patrol inquiries:</p>
        <p class="value">(555) 014-2087</p>
      </div>
    </div>
    <p class="web">www.ironwellsecurity.com</p>
  </footer>
</main>
</body>
</html>
```